Billboard Design for Equipment Rental Business

We need a billboard design for our equipment rental business called Brindlewood Equipment Company. We are based in Georgia. We rent construction tools, equipment, and dumpsters. We currently have a design but feel like we could get something better. Our phone number is 912-730-2591 and our website is www.brindlewoodequipment-example.com

```html
<!DOCTYPE html>
<html lang="en">
<head>
<meta charset="utf-8">
<title>Brindlewood Equipment Company – Billboard</title>
<link rel="stylesheet" href="https://fonts.googleapis.com/css2?family=Poppins:ital,wght@1,800&family=Roboto+Condensed:ital,wght@0,700;1,700&display=swap">
<style>
  :root {
    --board-yellow: #f9c021;
    --ink: #000000;
    --paper: #ffffff;
    --rule-dark: #3a2d08;
  }
  * { margin: 0; padding: 0; box-sizing: border-box; }
  html, body {
    width: 1200px;
    height: 624px;
    overflow: hidden;
    background: var(--paper);
  }
  .billboard {
    position: absolute;
    left: 88px;
    top: 76px;
    width: 1025px;
    height: 473px;
    background: var(--board-yellow);
    box-shadow: 0 2px 8px rgba(0,0,0,0.18);
    overflow: hidden;
  }
  .band-art {
    position: absolute;
    left: 0;
    top: 0;
    width: 1025px;
    height: 473px;
  }
  .brand {
    position: absolute;
    left: 52px;
    top: 246px;
    width: 335px;
    font-family: "Roboto Condensed", sans-serif;
    font-weight: 700;
    color: var(--ink);
    line-height: 1;
  }
  .brand-name {
    display: block;
    font-size: 55px;
    letter-spacing: 0.5px;
  }
  .brand-tag {
    display: block;
    margin-top: 22px;
    padding-left: 4px;
    font-size: 31px;
    letter-spacing: 2.2px;
  }
  .services {
    list-style: none;
    position: absolute;
    left: 531px;
    top: 0;
    font-family: "Poppins", sans-serif;
    font-style: italic;
    font-weight: 800;
    color: var(--ink);
    line-height: 1;
  }
  .service {
    position: absolute;
    left: 0;
    font-size: 75px;
    letter-spacing: -1px;
    white-space: nowrap;
  }
  .service--equipment { top: 46px; }
  .service--dumpsters { top: 134px; }
  .service--tools { top: 221px; left: 6px; }
  .service-rule {
    position: absolute;
    left: 472px;
    width: 553px;
    height: 2px;
    background: linear-gradient(90deg, rgba(58,45,8,0) 0%, var(--rule-dark) 40%, var(--ink) 55%, var(--rule-dark) 75%, rgba(58,45,8,0) 100%);
  }
  .service-rule--1 { top: 127px; }
  .service-rule--2 { top: 216px; }
  .service-rule--3 { top: 305px; }
  .phone {
    position: absolute;
    left: 64px;
    top: 381px;
    font-family: "Roboto Condensed", sans-serif;
    font-weight: 700;
    font-size: 48px;
    letter-spacing: 1px;
    line-height: 1;
    color: var(--paper);
  }
  .website {
    position: absolute;
    left: 558px;
    top: 392px;
    width: 440px;
    font-family: "Roboto Condensed", sans-serif;
    font-style: italic;
    font-weight: 700;
    font-size: 27px;
    line-height: 1;
    color: var(--ink);
    white-space: nowrap;
  }
</style>
</head>
<body>
  <div class="billboard">
    <svg class="band-art" viewBox="0 0 2200 1016" preserveAspectRatio="none" aria-hidden="true">
      <polygon fill="#000" points="934,760 2200,760 2200,1016 710,1016 780,936 0,936 0,808 892,808"/>
      <polygon fill="#f9c021" points="955,808 1030,808 919,936 844,936"/>
      <polygon fill="#f9c021" points="1080,808 1155,808 1044,936 967,936"/>
      <polygon fill="#f9c021" points="1209,808 2200,808 2200,936 1097,936"/>
    </svg>

    <div class="brand">
      <span class="brand-name">BRINDLEWOOD</span>
      <span class="brand-tag">EQUIPMENT COMPANY</span>
    </div>

    <ul class="services">
      <li class="service service--equipment">EQUIPMENT</li>
      <li class="service service--dumpsters">DUMPSTERS</li>
      <li class="service service--tools">TOOLS</li>
    </ul>
    <span class="service-rule service-rule--1"></span>
    <span class="service-rule service-rule--2"></span>
    <span class="service-rule service-rule--3"></span>

    <p class="phone">912-730-2591</p>
    <p class="website">www.brindlewoodequipment-example.com</p>
  </div>
</body>
</html>
```